Criação de Papelaria para Arquitetura
A empresa queria:
" Escritório fundado por dois sócios ( Bordalo & Quintela ) com atuação desde a criação do projeto arquitetônico, compatibilização de projetos complementares e a construção - gerenciamento de obras. Maiores informações: www.bqarquitetos-exemplo.com.br "

```html
<!DOCTYPE html>
<html lang="pt-BR">
<head>
<meta charset="utf-8">
<title>Bordalo &amp; Quintela — Blocos de Anotação</title>
<link rel="stylesheet" href="https://fonts.googleapis.com/css2?family=Raleway:wght@300;400&display=swap">
<style>
  :root {
    --bg: #e8e8e8;
    --paper: #ffffff;
    --ink: #1a1a1a;
    --cover: #0b0b0b;
    --rule: #9a9a9a;
    --muted: #555555;
    --edge: #cfd3d8;
  }
  * { box-sizing: border-box; margin: 0; padding: 0; }
  html, body { width: 1200px; height: 1200px; overflow: hidden; }
  body {
    background: var(--bg);
    font-family: "Raleway", sans-serif;
    font-weight: 300;
    color: var(--ink);
    display: flex;
    align-items: center;
    justify-content: center;
    gap: 45px;
  }
  .pad {
    width: 340px;
    height: 500px;
    position: relative;
    box-shadow: 0 0 0 1px var(--edge), 0 6px 0 -1px var(--edge);
  }
  .pad--cover { background: var(--cover); color: var(--paper); }
  .pad--letterhead, .pad--lined { background: var(--paper); }

  .brand {
    display: flex;
    align-items: center;
    gap: 10px;
    font-weight: 300;
    white-space: nowrap;
  }
  .brand__mark { width: 12px; height: 12px; background: currentColor; flex: none; }

  .pad--cover .brand {
    position: absolute; left: 0; right: 0; top: 232px;
    justify-content: center; font-size: 30px;
  }
  .pad--letterhead .brand {
    position: absolute; left: 30px; top: 150px; font-size: 30px;
  }

  .contact {
    position: absolute; left: 30px; right: 24px; bottom: 28px;
    display: grid; grid-template-columns: 1fr 1fr; gap: 6px 14px;
    font-size: 7.5px; font-weight: 400; color: var(--muted);
  }
  .contact__item { display: flex; align-items: center; gap: 5px; white-space: nowrap; }
  .contact__icon { width: 10px; height: 10px; flex: none; }

  .pad--lined .brand {
    position: absolute; left: 24px; top: 26px; font-size: 15px; gap: 6px;
  }
  .pad--lined .brand__mark { width: 7px; height: 7px; }
  .date-line {
    position: absolute; right: 24px; top: 36px;
    display: flex; gap: 6px; font-size: 9px; color: var(--muted);
  }
  .date-line span { width: 22px; border-bottom: 1px solid var(--rule); }
  .lines {
    position: absolute; left: 24px; right: 24px; top: 78px; bottom: 30px;
    background: repeating-linear-gradient(to bottom, transparent 0 23px, var(--rule) 23px 24px);
  }
</style>
</head>
<body>
  <section class="pad pad--cover" aria-label="Capa do bloco">
    <div class="brand"><span class="brand__mark"></span>Bordalo &amp; Quintela</div>
  </section>

  <section class="pad pad--letterhead" aria-label="Folha timbrada">
    <div class="brand"><span class="brand__mark"></span>Bordalo &amp; Quintela</div>
    <div class="contact">
      <div class="contact__item">
        <svg class="contact__icon" viewBox="0 0 10 10"><rect width="10" height="10" fill="#1a1a1a"/><path d="M3 2.5h1.2l.6 1.5-.8.6a4 4 0 0 0 1.4 1.4l.6-.8 1.5.6V7a.6.6 0 0 1-.6.6A4.6 4.6 0 0 1 2.4 3.1.6.6 0 0 1 3 2.5z" fill="#fff"/></svg>
        (11) 4000-0000
      </div>
      <div class="contact__item">
        <svg class="contact__icon" viewBox="0 0 10 10"><rect width="10" height="10" fill="#1a1a1a"/><path d="M5 2a2 2 0 0 1 2 2c0 1.5-2 4-2 4S3 5.5 3 4a2 2 0 0 1 2-2z" fill="#fff"/></svg>
        Rua Exemplo, 100 – São Paulo
      </div>
      <div class="contact__item">
        <svg class="contact__icon" viewBox="0 0 10 10"><rect width="10" height="10" fill="#1a1a1a"/><rect x="2" y="3" width="6" height="4" fill="none" stroke="#fff" stroke-width=".8"/><path d="M2 3l3 2.2L8 3" fill="none" stroke="#fff" stroke-width=".8"/></svg>
        contato@bqarquitetos-exemplo.com.br
      </div>
      <div class="contact__item">
        <svg class="contact__icon" viewBox="0 0 10 10"><rect width="10" height="10" fill="#1a1a1a"/><circle cx="5" cy="5" r="2.8" fill="none" stroke="#fff" stroke-width=".7"/><path d="M2.2 5h5.6M5 2.2v5.6" stroke="#fff" stroke-width=".6"/></svg>
        www.bqarquitetos-exemplo.com.br
      </div>
    </div>
  </section>

  <section class="pad pad--lined" aria-label="Folha pautada">
    <div class="brand"><span class="brand__mark"></span>Bordalo &amp; Quintela</div>
    <div class="date-line"><span></span>/<span></span>/<span></span></div>
    <div class="lines"></div>
  </section>
</body>
</html>
```